IT Consulting, IT Guru, Software Development, Network Solutions, Hosting

Attached is logo for our company, we just was the designers to come up with creative ideas to use the logo and the theme to come with creative and energetic business cards that leave an impression and stick in people's head.

Target Market(s)

Medical, Law, Entertainment, Real estate, any small to medium size business.

Industry/Entity Type

Business

Font styles to use
Serif
Sans Serif

```html
<!DOCTYPE html>
<html lang="en">
<head>
<meta charset="utf-8">
<title>BYTEVOLT Business Card</title>
<link href="https://fonts.googleapis.com/css2?family=Questrial&display=swap" rel="stylesheet">
<style>
  :root {
    --bg: #e9e7e3;
    --card-black: #161616;
    --card-black-edge: #262626;
    --card-white: #ffffff;
    --card-white-shade: #ececec;
    --accent-yellow: #f3c613;
    --ink-dark: #1c1c1c;
    --ink-light: #f4f4f4;
  }
  * { margin: 0; padding: 0; box-sizing: border-box; }
  html, body { width: 1200px; height: 784px; overflow: hidden; }
  body {
    background: var(--bg);
    font-family: "Questrial", "Century Gothic", sans-serif;
    position: relative;
  }
  .card {
    position: absolute;
    width: 520px;
    height: 298px;
    top: 243px;
    overflow: hidden;
    box-shadow: 0 10px 28px rgba(0,0,0,0.18);
  }
  .card--back {
    left: 50px;
    background: radial-gradient(ellipse at 50% 40%, var(--card-black-edge), var(--card-black) 75%);
    display: flex;
    align-items: center;
    justify-content: center;
  }
  .card--front { left: 630px; background: var(--card-black); }

  .brand-name {
    font-size: 64px;
    letter-spacing: 2px;
    line-height: 1;
    font-weight: 400;
  }
  .card--back .brand-name { color: var(--accent-yellow); }

  .front-top {
    position: absolute;
    left: 0; top: 0;
    width: 100%;
    height: 136px;
    background: linear-gradient(180deg, var(--card-white) 0%, var(--card-white-shade) 100%);
    display: flex;
    align-items: center;
    justify-content: center;
    padding-top: 10px;
  }
  .card--front .brand-name { color: var(--ink-dark); font-size: 60px; }
  .front-rule {
    position: absolute;
    left: 0; top: 136px;
    width: 100%;
    height: 7px;
    background: var(--accent-yellow);
  }
  .contact-list {
    position: absolute;
    left: 30px;
    top: 162px;
    list-style: none;
    color: var(--ink-light);
    font-size: 17px;
    line-height: 24px;
  }
  .contact-item { display: flex; align-items: center; gap: 10px; }
  .contact-item--plain { padding-left: 28px; }
  .contact-icon { width: 18px; height: 18px; flex: none; }
</style>
</head>
<body>

<section class="card card--back" aria-label="Business card back">
  <span class="brand-name">BYTEVOLT</span>
</section>

<section class="card card--front" aria-label="Business card front">
  <div class="front-top">
    <span class="brand-name">BYTEVOLT</span>
  </div>
  <div class="front-rule"></div>

  <ul class="contact-list">
    <li class="contact-item">
      <svg class="contact-icon" viewBox="0 0 24 24" aria-hidden="true">
        <path d="M6.6 10.8a15 15 0 0 0 6.6 6.6l2.2-2.2a1 1 0 0 1 1-.25 11.4 11.4 0 0 0 3.6.6 1 1 0 0 1 1 1V20a1 1 0 0 1-1 1A17 17 0 0 1 3 4a1 1 0 0 1 1-1h3.5a1 1 0 0 1 1 1c0 1.25.2 2.45.6 3.6a1 1 0 0 1-.25 1z" fill="var(--accent-yellow)"/>
      </svg>
      <span>1800-555-0147</span>
    </li>
    <li class="contact-item">
      <svg class="contact-icon" viewBox="0 0 24 24" aria-hidden="true">
        <rect x="2" y="5" width="20" height="14" rx="1.5" fill="var(--accent-yellow)"/>
        <path d="M2.5 6l9.5 7 9.5-7" fill="none" stroke="var(--card-black)" stroke-width="1.6"/>
      </svg>
      <span>info@bytevolt.com</span>
    </li>
    <li class="contact-item">
      <svg class="contact-icon" viewBox="0 0 24 24" aria-hidden="true">
        <g fill="none" stroke="var(--accent-yellow)" stroke-width="1.8">
          <circle cx="12" cy="12" r="9.5"/>
          <ellipse cx="12" cy="12" rx="4.2" ry="9.5"/>
          <path d="M2.5 12h19M4 7h16M4 17h16"/>
        </g>
      </svg>
      <span>www.bytevolt.com</span>
    </li>
    <li class="contact-item">
      <svg class="contact-icon" viewBox="0 0 24 24" aria-hidden="true">
        <path d="M12 3l10 8.5h-3V21h-5v-6h-4v6H5v-9.5H2z" fill="var(--accent-yellow)"/>
      </svg>
      <span>2150 Harbor Ave. Suite 410</span>
    </li>
    <li class="contact-item contact-item--plain">
      <span>Coral Bay, Fl 33099</span>
    </li>
  </ul>
</section>

</body>
</html>
```